Specialist Recruitment Process Outsourcing (RPO) company needs a modern, sleek website

We need a website which showcases our service offering, describes our onshore and offshore options. Our service is basically building teams of recruiters who become the outsourced (but in-house) recruiter for that specific client. Our logo colours include a light, bright green and a dark/midnight blue. This company will be targeting companies who need help with recruitment in technology, finance, engineering and other white collar industries. We are looking for a look and feeling that communicates cutting edge technology with a bright, energetic appeal. I will include some logo design files to work with.

Target Market(s)

Businesses: start ups who need to grow their staff, SMEs with regular recruitment needs, and larger businesses

Industry/Entity Type

Recruitment

Coding

Coded - Design and coding required

Number of Pages Required

4 page

Font styles to use
Sans Serif

Requirements
Must have
• Landing page should be highly visual, either with dynamic image or scrolling stills accompanies by our core service offering, values, and benefits.

A Services page will allows more detail about what we do, with a call to action.

A User Stories page will showcase some examples of how our services will help certain types of businesses.

Onshore/Offshore page will breakdown the benefits of both approaches and how combinations can work well.

Should fit the colour theming of our logo (files uploaded).

Nice to have
• Imagery can be both around business and people. We are looking for more of a "startup" feel than a corporate-y feel.

```html
<!DOCTYPE html>
<html lang="en">
<head>
<meta charset="utf-8">
<title>Hireloom — Specialist Recruitment</title>
<link href="https://fonts.googleapis.com/css2?family=Michroma&family=Lato:ital,wght@0,400;0,700;0,900;1,400;1,700&family=Oswald:wght@500&display=swap" rel="stylesheet">
<style>
:root{
  --green:#1ee8a4;
  --green-dark:#11b67f;
  --navy:#0d1533;
  --navy-mid:#141b47;
  --ink:#1b1b1b;
  --muted:#6b6f78;
  --line:#e7e9ee;
  --white:#ffffff;
  --footer:#0b0b0c;
}
*{box-sizing:border-box;margin:0;padding:0}
html,body{width:1200px;height:4563px;overflow:hidden}
body{position:relative;background:var(--white);font-family:'Lato',sans-serif;color:var(--ink)}
.abs{position:absolute}
.display{font-family:'Michroma',sans-serif;font-weight:400;letter-spacing:1px;line-height:1.2}

/* header */
.site-header{left:0;top:0;width:1200px;height:68px;background:var(--white)}
.brand{left:100px;top:6px;width:130px;height:56px;display:flex;align-items:center;gap:8px}
.brand-dot{width:14px;height:14px;border-radius:50%;background:var(--navy)}
.brand-name{font-family:'Lato',sans-serif;font-weight:700;font-size:16px;letter-spacing:2px;color:var(--navy)}
.search{left:522px;top:11px;width:282px;height:46px;border:1px solid #cfd3da;border-radius:23px}
.search span{position:absolute;left:18px;top:14px;font-size:12px;color:#8a8f98}
.search-btn{position:absolute;right:2px;top:2px;width:40px;height:40px;border-radius:50%;background:var(--navy)}
.flag{left:826px;top:15px;width:40px;height:40px;border-radius:50%;background:linear-gradient(180deg,#2b3f8f 0 45%,#d9333f 45% 60%,#f2f2f2 60% 75%,#d9333f 75%)}
.social-top{left:904px;top:16px;display:flex;gap:7px}
.social-top i{display:block;width:33px;height:33px;border:1.5px solid #333;border-radius:50%}

.main-nav{left:0;top:68px;width:1200px;height:51px;background:var(--navy)}
.main-nav a{position:absolute;top:0;height:51px;line-height:51px;color:var(--white);font-weight:700;font-size:15px;text-decoration:none;transform:translateX(-50%);white-space:nowrap}
.main-nav a.active{background:var(--green);padding:0 10px}

/* hero */
.hero{left:0;top:119px;width:1200px;height:608px;background:linear-gradient(180deg,#9c9a96 0%,#b2afaa 40%,#6e6a65 75%,#3a3835 100%)}
.hero-title{left:129px;top:292px;font-size:44px;line-height:52px;color:var(--white);white-space:nowrap}
.hero-text{left:129px;top:352px;width:480px;font-size:13.5px;line-height:28px;color:#f2f2f2}
.btn{display:block;background:var(--green);color:var(--white);font-weight:900;font-size:15px;text-align:center;border-radius:26px;text-decoration:none}
.hero-btn{left:129px;top:431px;width:176px;height:46px;line-height:46px}
.slide-arrow{width:38px;height:38px;border:1.5px solid rgba(255,255,255,.7);border-radius:50%}
.dots{display:flex;gap:6px}
.dots i{display:block;width:11px;height:11px;border-radius:50%;background:#c8c8c8}
.dots i.on{background:var(--green)}

/* about */
.about-mark{left:110px;top:815px;width:475px;height:334px;display:flex;align-items:center;justify-content:center;gap:14px}
.about-mark .brand-dot{width:30px;height:30px;background:var(--green-dark)}
.about-mark span{font-weight:700;font-size:40px;letter-spacing:4px;color:var(--green-dark)}
.section-title{font-size:36px;color:var(--ink)}
.about-title{left:631px;top:806px}
.body-copy{font-size:13px;line-height:28.4px;color:var(--muted)}
.about-copy{left:631px;top:862px;width:455px}
.about-btn{left:631px;top:1099px;width:175px;height:48px;line-height:48px}

/* offer */
.offer{left:0;top:1227px;width:1200px;height:755px;background:linear-gradient(135deg,#0e3a2e 0%,#1f5a44 35%,#163a30 60%,#0c2a22 100%)}
.offer-title{left:0;top:1312px;width:1200px;text-align:center;font-size:34px;color:var(--white)}
.offer-sub{left:240px;top:1369px;width:720px;text-align:center;font-size:13.5px;line-height:28px;color:var(--white);font-weight:700}
.offer-card{width:461px;height:213px;background:var(--white)}
.offer-card svg{position:absolute;left:40px;top:68px}
.card-title{position:absolute;left:127px;top:38px;font-family:'Oswald',sans-serif;font-weight:500;font-size:21px;color:var(--ink)}
.card-copy{position:absolute;left:127px;top:76px;width:300px;font-size:12px;line-height:25px;color:var(--muted)}

/* value */
.value-title{left:110px;top:2057px}
.value-sub{left:110px;top:2113px;font-size:16px;color:var(--ink)}
.value-copy{left:110px;top:2150px;width:490px;text-align:justify}
.value-photo{left:629px;top:1982px;width:571px;height:407px;background:linear-gradient(100deg,#d9dde2 0%,#8a97ad 35%,#2f4374 60%,#c9cfd7 85%,#eef0f2 100%)}

/* testimonials */
.testimonials{left:0;top:2389px;width:1200px;height:447px;background:var(--navy-mid)}
.testi-title{left:0;top:2504px;width:1200px;text-align:center;font-size:28px;color:var(--white)}
.avatar{left:214px;top:2570px;width:105px;height:105px;border-radius:50%;background:linear-gradient(180deg,#d7d7d7,#8e8a86);border:3px solid var(--white)}
.testi-name{left:200px;top:2687px;width:134px;text-align:center;color:var(--white);font-weight:700;font-size:15px}
.stars{left:200px;top:2707px;width:134px;text-align:center;color:#f0c43a;font-size:10px;letter-spacing:1px}
.quote{left:377px;top:2586px;width:605px;color:var(--white);font-style:italic;font-size:15px;line-height:28.4px}
.qmark{font-family:Georgia,serif;font-size:54px;color:#7d8296;line-height:1}
.side-arrow{width:92px;height:92px;border-radius:50%;background:#3b4157}

/* benefits */
.benefits-title{left:0;top:2908px;width:1200px;text-align:center;font-size:36px;color:var(--ink)}
.benefit{width:316px;height:296px;background:var(--white);box-shadow:0 0 10px rgba(0,0,0,.12);border-bottom:5px solid var(--green);text-align:center}
.benefit svg{position:absolute;left:120px;top:38px}
.benefit h3{position:absolute;left:0;top:128px;width:100%;font-family:'Oswald',sans-serif;font-weight:500;font-size:21px;color:var(--ink)}
.benefit p{position:absolute;left:12px;top:166px;width:292px;font-size:12.5px;line-height:25.7px;color:var(--muted)}

/* cta */
.cta-photo{left:0;top:3683px;width:1200px;height:505px;background:linear-gradient(180deg,#e9e7e3 0%,#cfccc6 35%,#4a4d55 70%,#e4e3e0 100%)}
.bubble{border-radius:50%;text-align:center;display:flex;flex-direction:column;align-items:center;justify-content:center}
.bubble-navy{left:329px;top:3965px;width:164px;height:164px;background:var(--navy);color:var(--white);font-size:15px;line-height:23px}
.bubble-white{left:487px;top:3902px;width:242px;height:242px;background:var(--white);border:2px solid #eee;color:#333;font-size:24px;line-height:33px}
.bubble-green{left:695px;top:3843px;width:170px;height:170px;background:var(--green);color:var(--white);font-size:15px;line-height:23px}
.bubble a{color:inherit;font-weight:700;font-size:14px;margin-top:8px;text-decoration:underline}
.job-btn{margin-top:12px;width:128px;height:38px;line-height:38px;border-radius:20px;background:var(--green);color:var(--white);font-weight:900;font-size:16px}

/* footer */
.footer{left:0;top:4188px;width:1200px;height:375px;background:var(--footer)}
.footer-brand{left:110px;top:4370px;display:flex;align-items:center;gap:14px}
.footer-brand .brand-dot{width:22px;height:22px;background:var(--white)}
.footer-brand span{color:var(--white);font-weight:700;font-size:26px;letter-spacing:6px}
.f-head{color:var(--white);font-weight:700;font-size:16px}
.f-list{list-style:none;color:var(--white);font-size:12.5px;line-height:25.7px}
.f-row{display:flex;gap:10px;color:var(--white);font-size:12.5px;line-height:26px}
.f-social{left:890px;top:4345px;display:flex;gap:8px}
.f-social i{display:block;width:34px;height:34px;border-radius:50%;background:var(--white)}
.copyright{left:0;top:4516px;width:1200px;text-align:center;color:var(--white);font-size:12.5px}
</style>
</head>
<body>

<header class="abs site-header">
  <div class="abs brand"><i class="brand-dot"></i><span class="brand-name">HIRELOOM</span></div>
  <div class="abs search"><span>Search</span>
    <div class="search-btn"><svg width="40" height="40" viewBox="0 0 40 40"><circle cx="18" cy="18" r="7" fill="none" stroke="#fff" stroke-width="2"/><line x1="23" y1="23" x2="28" y2="28" stroke="#fff" stroke-width="2"/></svg></div>
  </div>
  <div class="abs flag" role="img" aria-label="Language selector flag"></div>
  <svg class="abs" style="left:872px;top:31px" width="12" height="8" viewBox="0 0 12 8"><path d="M1 1l5 5 5-5" fill="none" stroke="#555" stroke-width="1.5"/></svg>
  <div class="abs social-top"><i></i><i></i><i></i><i></i><i></i></div>
</header>

<nav class="abs main-nav">
  <a class="active" style="left:143px">HOME</a>
  <a style="left:269px">ABOUT</a>
  <a style="left:425px">OUR SERVICES</a>
  <a style="left:608px">USER STORIES</a>
  <a style="left:821px">ONSHORE/OFFSHORE</a>
  <a style="left:1030px">CONTACT US</a>
</nav>

<section class="abs hero" role="img" aria-label="Photo of a diverse team working together at a meeting table with laptops"></section>
<h1 class="abs display hero-title">HIRELOOM</h1>
<p class="abs hero-text">Lorem ipsum dolor sit amet, consectetur adipiscing elit, sed do eiusmod tempor incididunt ut labore et dolore magna aliqua.</p>
<a class="abs btn hero-btn">GET STARTED</a>
<div class="abs slide-arrow" style="left:62px;top:404px"><svg width="36" height="36"><path d="M21 11l-7 7 7 7" fill="none" stroke="#fff" stroke-width="1.5"/></svg></div>
<div class="abs slide-arrow" style="left:1101px;top:404px"><svg width="36" height="36"><path d="M15 11l7 7-7 7" fill="none" stroke="#fff" stroke-width="1.5"/></svg></div>
<div class="abs dots" style="left:570px;top:664px"><i class="on"></i><i></i><i class="on"></i><i></i></div>

<div class="abs about-mark" role="img" aria-label="Hireloom brand mark"><i class="brand-dot"></i><span>HIRELOOM</span></div>
<h2 class="abs display section-title about-title">ABOUT US</h2>
<p class="abs body-copy about-copy">Lorem ipsum dolor sit amet, consectetur adipiscing elit, sed do eiusmod tempor incididunt ut labore et dolore magna aliqua. Quis ipsum suspendisse ultrices gravida. Risus commodo viverra maecenas accumsan lacus vel facilisis. Lorem ipsum dolor sit amet, consectetur adipiscing elit, sed do eiusmod tempor incididunt ut labore et dolore magna aliqua. Quis ipsum suspendisse ultrices gravida. Risus commodo viverra maecenas accumsan lacus vel facilisis. Lorem ipsum dolor sit amet, consectetur adipiscing elit, sed do eiusmod tempor incididunt ut labore</p>
<a class="abs btn about-btn">LEARN MORE</a>

<section class="abs offer" role="img" aria-label="Green tinted photo of city office towers"></section>
<h2 class="abs display offer-title">WHAT WE OFFER</h2>
<p class="abs offer-sub">Lorem ipsum dolor sit amet, consectetur adipiscing elit, sed do eiusmod tempor incididunt ut labore et dolore magna aliqua. Quis ipsum suspendisse ultrices gravida.</p>

<div class="abs offer-card" style="left:135px;top:1461px">
  <svg width="66" height="66" viewBox="0 0 66 66" fill="none" stroke="#1a9e73" stroke-width="2"><rect x="6" y="4" width="38" height="52" rx="2"/><line x1="12" y1="14" x2="30" y2="14"/><rect x="12" y="34" width="5" height="14"/><rect x="21" y="28" width="5" height="20"/><rect x="30" y="38" width="5" height="10"/><circle cx="48" cy="28" r="11"/><line x1="48" y1="23" x2="48" y2="33"/></svg>
  <h3 class="card-title">SOURCING</h3>
  <p class="card-copy">Lorem ipsum dolor sit a conseur piscing elit, sed do eiusmod tempor incididunt ut labore et dolore magna aliqua. Quis ipsum suspendisse ultrices gravida. Risus commodo</p>
</div>
<div class="abs offer-card" style="left:603px;top:1461px">
  <svg width="66" height="66" viewBox="0 0 66 66" fill="none" stroke="#1a9e73" stroke-width="2"><circle cx="33" cy="14" r="7"/><path d="M20 30l13 12 13-12"/><path d="M8 40l14 16M58 40L44 56"/><line x1="33" y1="21" x2="33" y2="42"/></svg>
  <h3 class="card-title">INTERVENTION</h3>
  <p class="card-copy">Lorem ipsum dolor sit a conseur piscing elit, sed do eiusmod tempor incididunt ut labore et dolore magna aliqua. Quis ipsum suspendisse ultrices gravida. Risus commodo</p>
</div>
<div class="abs offer-card" style="left:135px;top:1680px">
  <svg width="66" height="66" viewBox="0 0 66 66" fill="none" stroke="#1a9e73" stroke-width="2"><circle cx="14" cy="16" r="6"/><circle cx="33" cy="10" r="6"/><circle cx="52" cy="16" r="6"/><path d="M14 22v14M33 16v14M52 22v14"/><path d="M24 60V42h18v18"/></svg>
  <h3 class="card-title">SELECTION</h3>
  <p class="card-copy">Lorem ipsum dolor sit a conseur piscing elit, sed do eiusmod tempor incididunt ut labore et dolore magna aliqua. Quis ipsum suspendisse ultrices gravida. Risus commodo</p>
</div>
<div class="abs offer-card" style="left:603px;top:1680px">
  <svg width="66" height="66" viewBox="0 0 66 66" fill="none" stroke="#1a9e73" stroke-width="2"><circle cx="12" cy="12" r="5"/><circle cx="26" cy="12" r="5"/><circle cx="40" cy="12" r="5"/><rect x="6" y="24" width="40" height="10"/><rect x="6" y="38" width="40" height="10"/><circle cx="56" cy="30" r="5"/></svg>
  <h3 class="card-title">ON BOARDING</h3>
  <p class="card-copy">Lorem ipsum dolor sit a conseur piscing elit, sed do eiusmod tempor incididunt ut labore et dolore magna aliqua. Quis ipsum suspendisse ultrices gravida. Risus commodo</p>
</div>

<h2 class="abs display section-title value-title">OUR VALUE</h2>
<p class="abs value-sub">Specialist Recruitment!</p>
<p class="abs body-copy value-copy">Lorem ipsum dolor sit amet, consectetur adipiscing elit, sed do eiusmod tempor incididunt ut labore et dolore magna aliqua. Quis ipsum suspendisse ultrices gravida. Risus commodo viverra maecenas accumsan lacus vel facilisis. Lorem ipsum dolor sit amet, consectetur adipiscing elit, sed do eiusmod tempor incididunt ut labore et dolore magna aliqua. Quis ipsum suspendisse ultrices gravida. Risus commodo viverra maecenas accumsan lacus vel facilisis.</p>
<div class="abs value-photo" role="img" aria-label="Photo of business people shaking hands in a bright office"></div>

<section class="abs testimonials"></section>
<h2 class="abs display testi-title">WHAT OUR CUSTOMERS ARE SAYING</h2>
<div class="abs side-arrow" style="left:-46px;top:2584px"><svg class="abs" style="left:52px;top:34px" width="20" height="24"><path d="M13 3l-8 9 8 9" fill="none" stroke="#fff" stroke-width="1.5"/></svg></div>
<div class="abs side-arrow" style="left:1154px;top:2584px"><svg class="abs" style="left:20px;top:34px" width="20" height="24"><path d="M7 3l8 9-8 9" fill="none" stroke="#fff" stroke-width="1.5"/></svg></div>
<div class="abs avatar" role="img" aria-label="Portrait photo of the client"></div>
<p class="abs testi-name">- Daniel Reyes</p>
<p class="abs stars">★★★★★</p>
<span class="abs qmark" style="left:338px;top:2576px">“</span>
<p class="abs quote">Lorem ipsum dolor sit amet, consectetur adipiscing elit, sed do e incididunt ut labore et dolore magna aliqua. Quis ipsum suspendisse ultrices gravida. Risus commodo viverra maecenas accumsan lacus vel facilisis. Lorem ipsum dolor siet, consectetur adipiscing elit, sed do e incididunt ut labore et dolore magna aliqua.</p>
<span class="abs qmark" style="left:778px;top:2665px">”</span>
<div class="abs dots" style="left:568px;top:2735px"><i style="background:#fff"></i><i style="background:#8a8fa6"></i><i style="background:#8a8fa6"></i><i style="background:#8a8fa6"></i></div>

<h2 class="abs display benefits-title">OUR BENIFITS</h2>
<div class="abs benefit" style="left:112px;top:2992px">
  <svg width="76" height="76" viewBox="0 0 76 76" fill="none" stroke="#1a9e73" stroke-width="2"><circle cx="38" cy="38" r="32"/><ellipse cx="38" cy="38" rx="14" ry="32"/><line x1="6" y1="38" x2="70" y2="38"/><line x1="10" y1="22" x2="66" y2="22"/><line x1="10" y1="54" x2="66" y2="54"/></svg>
  <h3>The standard Lorem</h3><p>Lorem ipsum dolor sit amet, consectetur adipiscing elit, sed do eiusmod tempor incididunt ut labore et dolore magna aliqua. Quis ium suspendisse ultrices gravida. Risus commodo viverra</p>
</div>
<div class="abs benefit" style="left:443px;top:2992px">
  <svg width="76" height="76" viewBox="0 0 76 76" fill="none" stroke="#1a9e73" stroke-width="2"><path d="M38 6v26M38 6l-6 6M38 6l6 6M14 20l16 14M14 20v8M14 20h8M62 20L46 34M62 20v8M62 20h-8"/><circle cx="38" cy="48" r="10"/><path d="M26 72c0-8 6-12 12-12s12 4 12 12"/></svg>
  <h3>The standard Lorem</h3><p>Lorem ipsum dolor sit amet, consectetur adipiscing elit, sed do eiusmod tempor incididunt ut labore et dolore magna aliqua. Quis ium suspendisse ultrices gravida. Risus commodo viverra</p>
</div>
<div class="abs benefit" style="left:773px;top:2992px">
  <svg width="76" height="76" viewBox="0 0 76 76" fill="none" stroke="#1a9e73" stroke-width="2"><circle cx="38" cy="28" r="13"/><path d="M22 28a16 16 0 0132 0"/><rect x="18" y="26" width="6" height="10" rx="2"/><rect x="52" y="26" width="6" height="10" rx="2"/><path d="M12 72c0-14 12-22 26-22s26 8 26 22z"/></svg>
  <h3>The standard Lorem</h3><p>Lorem ipsum dolor sit amet, consectetur adipiscing elit, sed do eiusmod tempor incididunt ut labore et dolore magna aliqua. Quis ium suspendisse ultrices gravida. Risus commodo viverra</p>
</div>
<div class="abs benefit" style="left:112px;top:3300px">
  <svg width="76" height="76" viewBox="0 0 76 76" fill="none" stroke="#1a9e73" stroke-width="2"><path d="M6 66l20-20 12 10 30-34"/><path d="M56 22h12v12"/><circle cx="36" cy="12" r="6"/><path d="M36 18l-6 16 10 6"/></svg>
  <h3>The standard Lorem</h3><p>Lorem ipsum dolor sit amet, consectetur adipiscing elit, sed do eiusmod tempor incididunt ut labore et dolore magna aliqua. Quis ium suspendisse ultrices gravida. Risus commodo viverra</p>
</div>
<div class="abs benefit" style="left:443px;top:3300px">
  <svg width="76" height="76" viewBox="0 0 76 76" fill="none" stroke="#1a9e73" stroke-width="2"><rect x="18" y="6" width="52" height="42" rx="2"/><rect x="6" y="46" width="6" height="20"/><rect x="16" y="38" width="6" height="28"/><rect x="26" y="50" width="6" height="16"/><circle cx="48" cy="26" r="10"/><path d="M48 16v10h10"/></svg>
  <h3>The standard Lorem</h3><p>Lorem ipsum dolor sit amet, consectetur adipiscing elit, sed do eiusmod tempor incididunt ut labore et dolore magna aliqua. Quis ium suspendisse ultrices gravida. Risus commodo viverra</p>
</div>
<div class="abs benefit" style="left:773px;top:3300px">
  <svg width="76" height="76" viewBox="0 0 76 76" fill="none" stroke="#1a9e73" stroke-width="2"><rect x="10" y="6" width="56" height="64" rx="3"/><circle cx="38" cy="28" r="12"/><circle cx="38" cy="25" r="5"/><path d="M30 37c2-5 14-5 16 0"/><line x1="20" y1="50" x2="56" y2="50"/><line x1="20" y1="58" x2="56" y2="58"/></svg>
  <h3>The standard Lorem</h3><p>Lorem ipsum dolor sit amet, consectetur adipiscing elit, sed do eiusmod tempor incididunt ut labore et dolore magna aliqua. Quis ium suspendisse ultrices gravida. Risus commodo viverra</p>
</div>

<section class="abs cta-photo" role="img" aria-label="Photo of smiling job candidates seated in a row against a white brick wall"></section>
<div class="abs bubble bubble-navy"><span>Looking For<br>Career-Minded<br>Candidates?</span><a>Request Talent »</a></div>
<div class="abs bubble bubble-white"><span>excellence<br>in Hireloom<br>Team</span><span class="job-btn">JOB »</span></div>
<div class="abs bubble bubble-green"><span>Looking For<br>Career<br>Opportunities?</span><a>Search Jobs »</a></div>

<footer class="abs footer"></footer>
<div class="abs footer-brand"><i class="brand-dot"></i><span>HIRELOOM</span></div>
<p class="abs f-head" style="left:429px;top:4305px">QUICK LINKS</p>
<ul class="abs f-list" style="left:431px;top:4328px">
  <li>Home</li><li>About</li><li>Our Services</li><li>User Stories</li><li>Onshore/offshore</li><li>contact us</li>
</ul>
<p class="abs f-head" style="left:647px;top:4305px">FIND US</p>
<div class="abs f-row" style="left:645px;top:4337px">
  <svg width="12" height="16" viewBox="0 0 12 16" style="margin-top:5px"><path d="M6 0a6 6 0 00-6 6c0 4.5 6 10 6 10s6-5.5 6-10a6 6 0 00-6-6z" fill="#fff"/><circle cx="6" cy="6" r="2.2" fill="#0b0b0c"/></svg>
  <span>48 Harbor Lane, Westbrook<br>10150, United States</span>
</div>
<div class="abs f-row" style="left:645px;top:4393px">
  <svg width="12" height="14" viewBox="0 0 12 14" style="margin-top:6px"><path d="M2 0l3 3-1.5 2.5a8 8 0 004 4L10 8l2 3-2 3C5 14 0 8 0 2z" fill="#fff"/></svg>
  <span>555 014 2290</span>
</div>
<div class="abs f-row" style="left:645px;top:4431px">
  <svg width="14" height="11" viewBox="0 0 14 11" style="margin-top:8px"><rect width="14" height="11" fill="#fff"/><path d="M0 0l7 6 7-6" fill="none" stroke="#0b0b0c" stroke-width="1.2"/></svg>
  <span>info@hireloom.com</span>
</div>
<p class="abs f-head" style="left:895px;top:4305px">FOLLOW US</p>
<div class="abs f-social"><i></i><i></i><i></i><i></i><i></i></div>
<p class="abs copyright">Copyright © 2020 Hireloom. All rights reserved.</p>

</body>
</html>
```